Business Card Design needed for start up company Pramora

In need of a new business card designed for a start up company based in Sydney, Pramora is a new start up innovative Company, our mission it to make property accessible for everyday Australian and to become the leading Real Estate platform in Australia. We want it to be fresh and clean.

Industry/Entity Type

Financial

Contact Information for Business Card

Section for Name
Section for Title

PRAMORA - Where Doors Open Wide
Mobile:
Direct:

Font styles to use
Sans Serif

Colors
33a6d7
0692cd
0255a3
ffffff

Requirements
Must have
• Logo, all business card details

```html
<!DOCTYPE html>
<html lang="en">
<head>
<meta charset="utf-8">
<title>Pramora Business Card</title>
<link href="https://fonts.googleapis.com/css2?family=Poppins:wght@400;500;600&display=swap" rel="stylesheet">
<style>
  :root {
    --sky: #33a6d7;
    --ocean: #0692cd;
    --navy: #0255a3;
    --white: #ffffff;
    --ink: #3a3a3a;
    --rule: #8a8a8a;
    --backdrop: #2b2b2d;
  }
  * { margin: 0; padding: 0; box-sizing: border-box; }
  html, body { width: 1200px; height: 1000px; overflow: hidden; }
  body {
    background: var(--backdrop);
    font-family: "Poppins", sans-serif;
    position: relative;
  }
  .card {
    position: absolute;
    left: 340px;
    width: 520px;
    height: 300px;
    background: var(--white);
    border-radius: 26px;
    overflow: hidden;
    box-shadow: 0 10px 30px rgba(0,0,0,.45);
  }
  .card-front { top: 120px; }
  .card-back { top: 560px; }

  .brand-name {
    font-weight: 500;
    color: var(--navy);
    line-height: 1;
    letter-spacing: 0.5px;
  }

  .card-front .brand-name {
    position: absolute; left: 0; right: 0; top: 118px;
    text-align: center; font-size: 44px;
  }
  .tagline {
    position: absolute; left: 0; right: 0; top: 190px;
    text-align: center; color: var(--sky);
    font-size: 11px; letter-spacing: 3px;
  }

  .card-back .brand-name {
    position: absolute; right: 40px; top: 34px; font-size: 32px;
  }
  .holder { position: absolute; right: 40px; top: 92px; text-align: right; }
  .holder-name { font-size: 24px; font-weight: 600; line-height: 1.1; }
  .holder-first { color: var(--sky); }
  .holder-last { color: var(--navy); }
  .holder-title { font-size: 10px; color: var(--ink); margin-top: 2px; }
  .name-rule { position: absolute; left: 40px; top: 128px; width: 260px; height: 1px; background: var(--rule); }

  .contacts { position: absolute; right: 22px; top: 150px; list-style: none; }
  .contacts li {
    display: flex; justify-content: flex-end; align-items: center; gap: 8px;
    font-size: 11.5px; color: var(--ink); height: 17px;
  }
  .contacts svg { width: 10px; height: 10px; fill: var(--ocean); }
  .contacts .web-name { color: var(--ocean); }

  .address {
    position: absolute; left: 40px; top: 212px;
    display: flex; gap: 8px; font-size: 11.5px; color: var(--ink); line-height: 1.35;
  }
  .address svg { width: 11px; height: 11px; margin-top: 2px; fill: none; stroke: var(--navy); stroke-width: 1.6; }
  .band { position: absolute; left: 0; bottom: 0; width: 520px; height: 80px; }
</style>
</head>
<body>
  <section class="card card-front">
    <p class="brand-name">Pramora</p>
    <p class="tagline">Where Doors Open Wide</p>
  </section>

  <section class="card card-back">
    <p class="brand-name">Pramora</p>
    <div class="holder">
      <p class="holder-name"><span class="holder-first">Lena</span> <span class="holder-last">Hartley</span></p>
      <p class="holder-title">Founder / CEO</p>
    </div>
    <div class="name-rule"></div>
    <ul class="contacts">
      <li>000 123 456 789<svg viewBox="0 0 10 10"><path d="M2 0.5 L4 2.8 L3 4 Q4.3 6 6 7 L7.2 6 L9.5 8 L8 9.6 Q4 9.3 0.5 2 Z"/></svg></li>
      <li>000 222 3334<svg viewBox="0 0 10 10"><path d="M2.5 0 H7.5 V10 H2.5 Z M3.3 1 V8 H6.7 V1 Z"/></svg></li>
      <li>urname@email.com<svg viewBox="0 0 10 10"><path d="M0 2 H10 V8.5 H0 Z M0.8 2.6 L5 5.8 L9.2 2.6 Z" fill-rule="evenodd"/></svg></li>
      <li><span>www.<span class="web-name">websitename</span>.com</span><svg viewBox="0 0 10 10"><circle cx="5" cy="5" r="5"/></svg></li>
    </ul>
    <div class="address">
      <svg viewBox="0 0 12 12"><path d="M1 11 L6 1 L11 11 L6 8 Z"/></svg>
      <p>Your Street Address,<br>Sydney, 1234</p>
    </div>
    <svg class="band" viewBox="0 0 520 80" preserveAspectRatio="none" aria-hidden="true">
      <path d="M0 58 L330 58 Q345 58 352 46 Q360 32 378 32 L520 32 L520 80 L0 80 Z" fill="var(--navy)"/>
      <path d="M0 62 L332 62 Q348 62 356 50 Q364 36 380 36 L520 36 L520 80 L0 80 Z" fill="var(--white)"/>
      <path d="M0 66 L334 66 Q350 66 358 54 Q366 40 382 40 L520 40 L520 80 L0 80 Z" fill="var(--sky)"/>
    </svg>
  </section>
</body>
</html>
```